Lantern Stewardship Frame

I am looking for a graphic design of the attached leadership model. The colors and design can be altered in any manner that brings the model alive version of the house model.

```html
<!DOCTYPE html>
<html lang="en">
<head>
<meta charset="utf-8">
<title>Lantern Stewardship Frame</title>
<link rel="stylesheet" href="https://fonts.googleapis.com/css2?family=Open+Sans:wght@400;600&family=Source+Sans+3:wght@700&display=swap">
<style>
  :root {
    --navy: #3b5d96;
    --paper: #ffffff;
    --head-font: "Source Sans 3", sans-serif;
    --body-font: "Open Sans", sans-serif;
  }
  html, body { margin: 0; padding: 0; overflow: hidden; background: var(--paper); }
  .model { position: relative; width: 1200px; height: 1200px; overflow: hidden; background: var(--paper); color: var(--navy); font-family: var(--body-font); }
  .shapes { position: absolute; inset: 0; }
  .shapes .fill { fill: var(--navy); }
  .shapes .frame { fill: var(--paper); stroke: var(--navy); stroke-width: 14; }
  .banner-text { position: absolute; left: 0; width: 1200px; text-align: center; color: var(--paper); font-family: var(--head-font); font-weight: 700; line-height: 1; margin: 0; }
  .presence-title { top: 86px; font-size: 42px; }
  .outer-title { top: 244px; font-size: 42px; }
  .inner-title { top: 966px; font-size: 42px; }
  .tagline { position: absolute; top: 173px; left: 90px; width: 1020px; text-align: center; font-size: 28px; margin: 0; line-height: 1.2; white-space: nowrap; }
  .level-title { position: absolute; top: 354px; width: 365px; text-align: center; color: var(--paper); font-family: var(--head-font); font-weight: 700; font-size: 31px; margin: 0; line-height: 1; }
  .practice { position: absolute; top: 421px; margin: 0; }
  .practice h3 { font-weight: 400; font-size: 30px; text-decoration: underline; text-decoration-thickness: 1px; text-underline-offset: 5px; margin: 0 0 6px; line-height: 1.2; text-align: center; }
  .practice ul { list-style: none; margin: 0; padding: 0; }
  .practice li { position: relative; padding-left: 34px; font-size: 23.5px; line-height: 36px; letter-spacing: -0.3px; }
  .practice li::before { content: ""; position: absolute; left: 0; top: 9px; border-style: solid; border-width: 9px 0 9px 18px; border-color: transparent transparent transparent var(--navy); }
  .wellbeing { position: absolute; top: 1052px; margin: 0; padding: 0; list-style: none; }
  .wellbeing li { position: relative; padding-left: 22px; font-weight: 600; font-size: 24.5px; line-height: 39px; text-decoration: underline; text-decoration-thickness: 2px; text-underline-offset: 4px; }
  .wellbeing li::before { content: ""; position: absolute; left: 0; top: 15px; width: 11px; height: 11px; border-radius: 50%; background: var(--navy); }
</style>
</head>
<body>
<main class="model">
  <svg class="shapes" width="1200" height="1200" viewBox="0 0 1200 1200" aria-hidden="true">
    <rect class="frame" x="69" y="148" width="1083" height="120" rx="32"/>
    <path class="fill" d="M386,88 Q604,24 822,88 L822,148 L386,148 Z"/>
    <path class="fill" d="M36,227 L1171,227 L1171,284 Q604,340 36,284 Z"/>

    <path class="frame" d="M71,412 L71,889 Q71,920 102,920 L355,920 Q386,920 386,889 L386,412"/>
    <path class="frame" d="M457,412 L457,889 Q457,920 488,920 L741,920 Q772,920 772,889 L772,412"/>
    <path class="frame" d="M841,412 L841,889 Q841,920 872,920 L1125,920 Q1156,920 1156,889 L1156,412"/>

    <path class="fill" d="M48,337 Q230,319 413,337 L413,403 Q230,421 48,403 Z"/>
    <path class="fill" d="M431,337 Q613,319 796,337 L796,403 Q613,421 431,403 Z"/>
    <path class="fill" d="M817,337 Q999,319 1181,337 L1181,403 Q999,421 817,403 Z"/>

    <path class="frame" d="M63,1025 L63,1133 Q63,1167 97,1167 L1118,1167 Q1152,1167 1152,1133 L1152,1025"/>
    <rect class="fill" x="412" y="1025" width="9" height="142"/>
    <rect class="fill" x="784" y="1025" width="9" height="142"/>
    <path class="fill" d="M36,972 Q604,916 1171,972 L1171,1030 L36,1030 Z"/>
  </svg>

  <h1 class="banner-text presence-title">Presence</h1>
  <p class="tagline">Foster contagious success through people, relationships and a shared vision</p>
  <h2 class="banner-text outer-title">Outer (Impact) Strategies</h2>

  <h2 class="level-title" style="left:48px">Organization Level</h2>
  <h2 class="level-title" style="left:431px">Interpersonal Level</h2>
  <h2 class="level-title" style="left:817px">Personal Level</h2>

  <section class="practice" style="left:94px; width:270px">
    <h3 style="margin-left:-20px">Wins Theory</h3>
    <ul>
      <li>Develop concrete outcomes, and visible results</li>
      <li>Foster in-depth changes, and new practices</li>
      <li>Have a micro, inter-personal or local impact</li>
      <li>Cultivate positive judgement, and shared ambition</li>
    </ul>
  </section>

  <section class="practice" style="left:476px; width:272px">
    <h3 style="margin-left:-20px">Heart Listening</h3>
    <ul>
      <li>Ask open-ended questions</li>
      <li>Affirm someone’s strengths, efforts and past success</li>
      <li>Reflect back what is shared for confirma-tion</li>
      <li>Summarize key points to gain insights</li>
      <li>Share and develop mutual expertise</li>
    </ul>
  </section>

  <section class="practice" style="left:862px; width:290px">
    <h3 style="margin-left:-20px">Clear Dialogue</h3>
    <ul>
      <li>Pause</li>
      <li>Relax</li>
      <li>Open</li>
      <li>Attune to Emergence</li>
      <li>Listen Deeply</li>
      <li>Speak the Truth</li>
    </ul>
  </section>

  <h2 class="banner-text inner-title">Inner (Wellbeing) Strategies</h2>

  <ul class="wellbeing" style="left:100px">
    <li>Physical Fitness</li>
    <li>Nutrition</li>
  </ul>
  <ul class="wellbeing" style="left:466px">
    <li>Heart Rate Variability</li>
    <li>Neurofeedback</li>
  </ul>
  <ul class="wellbeing" style="left:833px">
    <li>Harbor Rambler Club</li>
    <li>Video Gaming Club</li>
  </ul>
</main>
</body>
</html>
```